Zielgruppe
Friseurin für Damen und Herren
Aufgabenstellung
https://lumiraschnitt.de
Bitte erstelle mir anhand der Daten von der Website einen angepassten Entwurf mit Neueröffnung und geben keine Preise an sondern die kunden sollen sich direkt eingeladen führen um persönlich vor Ort vorbei zuschauen.

```html
<!DOCTYPE html>
<html lang="de">
<head>
<meta charset="utf-8">
<title>Lumira Hair &amp; Beautylounge – Neueröffnung</title>
<link rel="stylesheet" href="https://fonts.googleapis.com/css2?family=Bodoni+Moda:wght@400&family=Montserrat:ital,wght@0,300;0,600;1,300&display=swap">
<style>
  :root {
    --sage: #6b7a58;
    --white: #ffffff;
    --ink: #141414;
    --blush: #e3c3b5;
    --blush-text: #efcdbf;
    --hair-light: #d49a66;
    --hair-mid: #a8623a;
    --hair-deep: #6e3820;
    --sky: #dfe6e6;
  }
  html, body { margin: 0; padding: 0; overflow: hidden; background: var(--white); }
  .flyer {
    position: relative;
    width: 1200px;
    height: 851px;
    overflow: hidden;
    background: var(--sage);
    font-family: "Montserrat", sans-serif;
  }
  .hair-photo { position: absolute; inset: 0; }
  .glasses-photo {
    position: absolute;
    left: 16px; top: 438px;
    width: 190px; height: 413px;
    background: linear-gradient(180deg, rgba(240,236,214,0.55) 0%, rgba(214,204,160,0.45) 55%, rgba(190,192,170,0.25) 100%);
    border-radius: 60px 60px 10px 10px;
    opacity: 0.7;
  }
  .frame {
    position: absolute;
    left: 57px; top: 60px;
    width: 1115px; height: 745px;
    border: 2px solid var(--white);
    box-sizing: border-box;
  }
  .logo-box {
    position: absolute;
    left: 180px; top: 0;
    width: 377px; height: 194px;
    background: var(--white);
    text-align: center;
    font-family: "Bodoni Moda", serif;
    font-weight: 400;
    color: var(--ink);
  }
  .logo-name {
    display: block;
    margin-top: 30px;
    font-size: 70px;
    line-height: 1;
    letter-spacing: -1px;
  }
  .logo-tag {
    display: block;
    margin-top: 14px;
    font-size: 27px;
    letter-spacing: -0.5px;
  }
  .brush-band { position: absolute; left: 0; top: 222px; width: 1030px; height: 156px; }
  .headline {
    position: absolute;
    left: 70px; top: 250px;
    margin: 0;
    font-family: "Bodoni Moda", serif;
    font-weight: 400;
    font-size: 84px;
    line-height: 1;
    color: var(--ink);
    letter-spacing: 0.5px;
  }
  .copy {
    position: absolute;
    left: 60px; width: 580px;
    margin: 0;
    text-align: center;
    color: var(--white);
    font-weight: 300;
    font-size: 18px;
    line-height: 29px;
    text-transform: uppercase;
  }
  .copy-intro { top: 430px; }
  .copy-invite { top: 563px; }
  .copy-invite strong { color: var(--blush-text); font-weight: 600; }
  .copy-closing { top: 645px; font-style: italic; }
</style>
</head>
<body>
<main class="flyer">
  <svg class="hair-photo" viewBox="0 0 1200 851" width="1200" height="851" role="img" aria-label="Foto: lange kupferrote, gelockte Haare">
    <defs>
      <linearGradient id="hairTone" x1="0" y1="0" x2="1" y2="1">
        <stop offset="0" stop-color="var(--hair-mid)"/>
        <stop offset="0.45" stop-color="var(--hair-light)"/>
        <stop offset="0.8" stop-color="var(--hair-mid)"/>
        <stop offset="1" stop-color="var(--hair-deep)"/>
      </linearGradient>
    </defs>
    <polygon points="707,0 1200,0 1200,851 600,851" fill="url(#hairTone)"/>
  </svg>

  <div class="glasses-photo" role="img" aria-label="Foto: zwei anstoßende Sektgläser"></div>

  <div class="frame"></div>

  <div class="logo-box">
    <span class="logo-name">LUMIRA</span>
    <span class="logo-tag">HAIR &amp; BEAUTYLOUNGE</span>
  </div>

  <svg class="brush-band" viewBox="0 0 1030 156" width="1030" height="156" aria-hidden="true">
    <path fill="var(--blush)" opacity="0.92"
      d="M0,8 L120,4 L300,10 L420,2 L560,12 L600,30 L650,38 L880,52 L960,60 L1000,74 L1030,92 L990,102 L900,116 L800,124 L760,140 L600,146 L420,152 L260,148 L120,156 L0,150 Z"/>
  </svg>

  <h1 class="headline">NEUERÖFFNUNG</h1>

  <p class="copy copy-intro">Schönheit und Stil in perfekter Harmonie –<br>dein neuer Friseursalon in Birkenstetten<br>für Damen &amp; Herren .</p>

  <p class="copy copy-invite">Wir laden dich herzlich zur Neueröffnung<br>der&nbsp; <strong>Lumira Hair &amp; Beautylounge</strong> ein.</p>

  <p class="copy copy-closing">Komm vorbei, lerne uns kennen<br>und entdecke deinen neuen Lieblingsplatz<br>für Haare &amp; Beauty.</p>
</main>
</body>
</html>
```